Tallow Ridge Snacks is looking for a wrapper design for our flagship protein bar. A sleek and simple, yet powerful design is a must. A company that has a no BS attitude, no flashy artwork and straight to the point advertising is key. Focusing on Bodybuilders and Powerlifters, the wrapper does not need to appeal to the mass market. A dark, simple, and powerful vibe must be achieved. Less is more

Target Market(s)

Body Builders and Powerlifters

Industry/Entity Type

Supplement

Font styles to use
Decorative

Colors

Designer to choose colors to be used in the design.

Requirements
Must have
• Refer to "Legal Label Requirements" document.
• Refer to "Template Drawn" or "Wrapper.ai" for dimensions.
• *Must have the "Tallow Bar" logo stamped somewhere on the front of the bar**
• Sleek and powerful design
• Neutral /dark colors and possible accents with logo colors (use sparingly)
• Flavor of bar "Peanut Butter Crisp" must be displayed somewhere. Simple graphic can be included if goes well with overall design.
• Wrapper will be foil, so please make use of metallic effects by leaving sections/outlines transparent.
• Claims: (State it uses "Hydrolyzed Whey Protein" and contains 25g's of protein and only 6g's of sugar, as well as only real ingredients (These must be in French as well)
• Proudly Canadian stamp with flag somewhere.
• Social Media Icons (Instagram,Facebook) as well as website "tallowbarsnx.ca)
• Design must be able to work with future bar flavors, with only altering colors/flavor graphic (if necessary)
• *Will Include Nutritional Label and Ingredient List at a later date*
Nice to have
• I think a cool graphic of a simple hand and hammer outline using the metallic effect would be cool. Something that resembles the act of "forging metal" while demonstrating power, but isn't too distracting.
• A label mock up to see a general bar idea
Should not have
• Flashy/godly designs

```html
<!DOCTYPE html>
<html lang="en">
<head>
<meta charset="utf-8">
<title>Tallow Bar – Peanut Butter Crisp wrapper</title>
<link rel="stylesheet" href="https://fonts.googleapis.com/css2?family=Oswald:wght@400;500;600&family=Roboto:wght@400;700&display=swap">
<style>
  :root{
    --stage:#e9e9e9;
    --wrap-dark:#151515;
    --wrap-mid:#232323;
    --panel-grey:#2e2e2e;
    --red:#e3191f;
    --red-deep:#b51217;
    --yellow:#f4d21b;
    --silver:#cfcfcf;
    --white:#ffffff;
    --ink:#111111;
  }
  *{box-sizing:border-box;margin:0;padding:0}
  html,body{width:899px;height:1200px;overflow:hidden;background:var(--stage)}
  body{position:relative;font-family:"Oswald",sans-serif;color:var(--white)}

  .wrapper{
    position:absolute;left:20px;top:290px;width:859px;height:619px;overflow:hidden;
    background:
      radial-gradient(circle at 1px 1px,rgba(255,255,255,.05) 1px,transparent 1.4px) 0 0/5px 5px,
      linear-gradient(180deg,#101010 0%,var(--wrap-mid) 45%,#1b1b1b 70%,#0e0e0e 100%);
  }
  .seal-end{
    position:absolute;right:0;top:0;width:70px;height:100%;
    background:repeating-linear-gradient(135deg,#2b2b2b 0 4px,#161616 4px 8px);
  }

  /* back (inverted) panel */
  .back-panel{position:absolute;left:0;top:0;width:859px;height:260px;transform:rotate(180deg)}
  .back-panel p{position:absolute;white-space:nowrap}
  .back-count{left:724px;top:44px;font-size:10px;color:var(--white)}
  .back-count span,.count span{color:var(--red)}
  .back-follow{left:84px;top:47px;font-size:10px;font-weight:500}
  .back-values{left:0;width:859px;text-align:center;top:80px;font-size:12px;color:#8a8a8a;letter-spacing:.5px}
  .back-story{left:0;width:859px;text-align:center;top:100px;font-size:7.5px;line-height:11px;color:var(--red)}
  .back-ingredients{left:0;width:859px;text-align:center;font-size:6.5px;color:#d9d9d9}
  .back-ingredients b{color:var(--red);font-weight:500}
  .back-ingredients.one{top:130px}
  .back-ingredients.two{top:156px}
  .back-contains{left:0;width:859px;text-align:center;top:180px;font-size:7px;color:var(--red)}

  /* front left emblem area */
  .emblem-panel{position:absolute;left:-74px;top:162px;width:296px;height:296px;border-radius:50%;background:var(--panel-grey)}
  .brand-stamp{position:absolute;left:75px;top:232px;width:110px;text-align:center}
  .brand-stamp .name{font-size:20px;font-weight:600;color:var(--red);letter-spacing:2px}
  .brand-stamp .motto{font-size:8px;letter-spacing:1px;line-height:10px;margin-top:4px}
  .claim-chips{position:absolute;left:79px;top:336px;display:flex;gap:8px}
  .chip{width:26px;height:30px;border-radius:5px;background:var(--red);border:1.5px solid var(--white);text-align:center;line-height:1}
  .chip b{display:block;font-size:10px;margin-top:5px;font-weight:600}
  .chip i{display:block;font-style:normal;font-size:5px;margin-top:2px}
  .site{position:absolute;left:86px;top:370px;font-size:8px;color:var(--red)}
  .count{position:absolute;font-size:10px}
  .count.front{left:76px;top:403px}
  .count.bottom{left:446px;top:536px}

  /* centre */
  .product-photo{position:absolute;left:204px;top:322px;width:78px;height:60px;border-radius:40% 10% 30% 50%;
    background:linear-gradient(135deg,#f0d9a2 0%,#c8904a 55%,#8a5a25 100%)}
  .wordmark{position:absolute;left:288px;top:258px;width:280px;text-align:center;font-size:46px;font-weight:500;letter-spacing:10px;color:var(--silver);line-height:1}
  .flavour{position:absolute;left:318px;top:362px;font-size:10.5px;white-space:nowrap}
  .flavour .red{color:var(--red)}
  .flavour .yellow{color:var(--yellow)}
  .dot{display:inline-block;width:7px;height:7px;border-radius:50%;background:var(--yellow);margin:0 3px 0 4px}

  /* claims banner */
  .claims-banner{position:absolute;left:617px;top:267px;width:242px;height:75px;background:var(--red);border-radius:38px 0 0 38px}
  .non-gmo{position:absolute;left:10px;top:18px;width:38px;height:38px;border-radius:50%;background:var(--red-deep);border:2px solid var(--white)}
  .canada-badge{position:absolute;left:160px;top:18px;width:36px;height:36px;border-radius:50%;border:2px solid var(--white)}
  .claim-list{position:absolute;list-style:none;font-size:8px;line-height:12.5px;font-weight:500}
  .claims-banner .claim-list{left:56px;top:7px}
  .claim-list li::before{content:"";display:inline-block;width:5px;height:5px;border-radius:50%;background:var(--white);margin-right:3px;vertical-align:1px}
  .claim-list.lower{left:446px;top:448px}
  .follow{position:absolute;font-size:10px;font-weight:500;white-space:nowrap}
  .follow.front{left:617px;top:402px}
  .follow.lower{left:446px;top:514px;font-size:8px}
  .follow em{font-style:normal;color:var(--red)}

  /* nutrition */
  .nutrition{position:absolute;left:77px;top:446px;width:355px;height:103px;background:var(--white);color:var(--ink);
    font-family:"Roboto",sans-serif;font-size:5.6px;display:flex;padding:3px;gap:4px;border:1px solid var(--ink)}
  .nutrition .head{width:84px;line-height:7px}
  .nutrition .title{font-size:10px;font-weight:700;line-height:10px}
  .nutrition .cal{font-size:7px;font-weight:700;margin-top:5px}
  .nutrition .demo{color:var(--red);font-family:"Oswald",sans-serif;font-size:7px;margin-top:14px}
  .nutrition table{border-collapse:collapse;width:128px;align-self:flex-start}
  .nutrition td{padding:.6px 1px;border-top:.5px solid #777}
  .nutrition td:last-child{text-align:right}
  .nutrition .col-head td{border-top:none;text-align:right;font-size:5px}
  .nutrition .foot{position:absolute;left:3px;bottom:1px;font-size:4.5px}

  .maker{position:absolute;left:587px;top:516px;font-size:8px;line-height:11px}
</style>
</head>
<body>
  <section class="wrapper" aria-label="Tallow Bar wrapper, flat layout">
    <div class="seal-end"></div>

    <div class="back-panel">
      <p class="back-count">50 <span>Bar / Barre</span></p>
      <p class="back-follow">Follow us at / Suivez nous sur: @tallowbar</p>
      <p class="back-values">Quality | Transparency | Results</p>
      <p class="back-story">Forged from the finest quality and performing ingredients: Tallow Bar delivers an outstanding macro-nutrient profile specifically<br>formulated for the power lifter and bodybuilder in mind.</p>
      <p class="back-ingredients one"><b>Ingredients:</b> Hydrolyzed whey protein, peanuts, peanut butter, brown rice crisps, honey, cocoa butter, sea salt and natural flavour, nothing else added.</p>
      <p class="back-ingredients two"><b>Ingrédients:</b> Protéine de lactosérum hydrolysée, arachides, beurre d'arachide, riz brun croustillant, miel, beurre de cacao, sel de mer.</p>
      <p class="back-contains">Contains: Milk, Peanuts / Contient: lait, arachides</p>
    </div>

    <div class="emblem-panel"></div>
    <div class="brand-stamp">
      <p class="name">TALLOW</p>
      <p class="motto">TALLOW STRONG MUSCLE<br>MUSCLE FORT TALLOW</p>
    </div>
    <div class="claim-chips">
      <div class="chip"><b>25G</b><i>Protein</i></div>
      <div class="chip"><b>6G</b><i>Sugar</i></div>
      <div class="chip"><b>GF</b><i>Gluten Free</i></div>
    </div>
    <p class="site">www.tallowbarsnx.ca</p>
    <p class="count front">50 <span>Bar / Barre</span></p>

    <div class="product-photo" role="img" aria-label="Peanut butter crisp bar with a swirl of peanut butter"></div>
    <p class="wordmark">TALLOW BAR</p>
    <p class="flavour">50 <span class="red">Bar / Barre</span> <span class="dot"></span><span class="yellow">Peanut Butter Crisp</span> <span class="dot"></span><span class="yellow">Crisp au beurre d'arachide</span></p>

    <div class="claims-banner">
      <div class="non-gmo"></div>
      <ul class="claim-list">
        <li>25g's of protein</li>
        <li>25g de protéines</li>
        <li>6g Sugar / Sucre</li>
        <li>Hydrolyzed Whey Protein</li>
        <li>Protéine de lactosérum hydrolysée</li>
      </ul>
      <div class="canada-badge"></div>
    </div>
    <p class="follow front">Follow us at / Suivez nous sur: <em>@tallowbar</em></p>

    <div class="nutrition">
      <div class="head">
        <p class="title">Nutrition Facts<br>Valeur nutritive</p>
        <p>Per 1 cup (122 g)<br>pour 1 tasse (122 g)</p>
        <p class="cal">Calories 140</p>
        <p>* DV = Daily Value<br>* VQ = valeur quotidienne</p>
        <p class="demo">DEMO NUTRITION FACTS</p>
      </div>
      <table>
        <tr class="col-head"><td colspan="2">% DV / % VQ*</td></tr>
        <tr><td>Fat / Lipides 8 g</td><td>11 %</td></tr>
        <tr><td>Saturated / saturés 3 g<br>+ Trans / trans 0 g</td><td>15 %</td></tr>
        <tr><td>Carbohydrate / Glucides 19 g</td><td></td></tr>
        <tr><td>Fibre / Fibres 2 g</td><td>7 %</td></tr>
        <tr><td>Sugars / Sucres 14 g</td><td>14 %</td></tr>
        <tr><td>Protein / Protéines 2 g</td><td></td></tr>
        <tr><td>Cholesterol / Cholestérol 0 mg</td><td></td></tr>
      </table>
      <table>
        <tr class="col-head"><td colspan="2">% DV / % VQ*</td></tr>
        <tr><td>Sodium 5 mg</td><td>1 %</td></tr>
        <tr><td>Potassium 200 mg</td><td>4 %</td></tr>
        <tr><td>Calcium 20 mg</td><td>2 %</td></tr>
        <tr><td>Iron / Fer 0.5 mg</td><td>3 %</td></tr>
        <tr><td>Vitamin A / Vitamine A 10 mcg</td><td>1 %</td></tr>
        <tr><td>Vitamin C / Vitamine C 14 mg</td><td>16 %</td></tr>
        <tr><td>Thiamine 0.05 mg</td><td>4 %</td></tr>
        <tr><td>Riboflavin / Riboflavine 0.05 mg</td><td>4 %</td></tr>
        <tr><td>Niacin / Niacine 0.75 mg</td><td>5 %</td></tr>
      </table>
      <p class="foot">* 5% or less is a little, 15% or more is a lot / 5% ou moins c'est peu, 15% ou plus c'est beaucoup</p>
    </div>

    <ul class="claim-list lower">
      <li>25g's of protein</li>
      <li>25g de protéines</li>
      <li>6g Sugar / Sucre</li>
      <li>Hydrolyzed Whey Protein</li>
      <li>Protéine de lactosérum hydrolysée</li>
    </ul>
    <p class="follow lower">Follow us at / Suivez nous sur: <em>@tallowbar</em></p>
    <p class="count bottom">50 <span>Bar / Barre</span></p>

    <p class="maker">Prairie Grain Food Works Inc.<br>18 Foundry Road<br>Brandell, SK S0K 4R2, Canada</p>
  </section>
</body>
</html>
```